Eye catching Stationary Design

Healthcare consultant firm looking for stationary design ( letterhead, envelope and business cards) That’s professional, classy and eye catching . The design should incorporate the logo and the colors of the logo in its design. You can see the logo on our website at www harbor key advisors. com.

```html
<!DOCTYPE html>
<html lang="en">
<head>
<meta charset="utf-8">
<title>Harbor Key Advisors – Stationery</title>
<link href="https://fonts.googleapis.com/css2?family=Cinzel:wght@500&family=Open+Sans:wght@400;600;700&family=Italianno&display=swap" rel="stylesheet">
<style>
:root{
  --bg:#dcdcdc;
  --paper:#f0efef;
  --navy:#0b4f98;
  --blue:#1f63aa;
  --sky:#3a9ad6;
  --deep:#134a8a;
  --ink:#555;
  --dark:#222;
}
*{margin:0;padding:0;box-sizing:border-box}
html,body{width:1200px;height:1037px;overflow:hidden;background:var(--bg)}
body{position:relative;font-family:'Open Sans',sans-serif;color:var(--ink)}
.sheet{position:absolute;background:var(--paper);box-shadow:0 2px 5px rgba(0,0,0,.18);overflow:hidden}
.wave{position:absolute;left:0;bottom:0;width:100%;display:block}
.brand{font-family:'Cinzel',serif;font-weight:500;color:var(--navy);white-space:nowrap;letter-spacing:0}
.brand.light{color:#fff}
.contact{font-size:6.4px;line-height:7.6px;color:var(--ink)}
.contact .row{display:flex;align-items:center;gap:3px}
.contact svg{width:5px;height:5px;fill:var(--navy);flex:none}

/* letterhead */
.letterhead{left:59px;top:167px;width:373px;height:525px;z-index:2}
.letterhead .brand{position:absolute;left:33px;top:38px;font-size:7px;line-height:9px}
.letterhead .divider{position:absolute;top:29px;width:1px;height:20px;background:#aaa}
.letterhead .contact{position:absolute;top:29px}
.letter{position:absolute;left:40px;top:114px;width:294px;font-size:5.9px;line-height:8.8px;color:var(--ink)}
.letter p{margin-bottom:8.7px;text-align:justify}
.letter .addr{margin-top:9px}
.letter strong{color:var(--dark);font-weight:700}
.letter .sign{font-family:'Italianno',cursive;font-size:15px;color:var(--dark);line-height:14px;margin-top:-6px}

/* folder */
.folder{position:absolute;left:474px;top:130px;width:441px;height:561px;background:linear-gradient(#2a69ad,#1f5c9f 45%,#134a8a);overflow:hidden;box-shadow:0 2px 6px rgba(0,0,0,.25)}
.folder .spine{position:absolute;top:0;bottom:0;width:2px;background:rgba(255,255,255,.12)}
.folder .brand{position:absolute;left:0;right:0;top:98px;text-align:center;font-size:14.5px}

/* business cards */
.card{width:188px;height:107px;left:953px}
.card.front{top:289px}
.card.front .brand{position:absolute;left:16px;top:50px;font-size:5.4px}
.card.front .divider{position:absolute;left:94px;top:30px;width:1px;height:48px;background:#bbb}
.card.front .details{position:absolute;left:103px;top:29px;font-size:4.2px;line-height:5.2px}
.card .name{font-family:'Cinzel',serif;color:var(--navy);font-size:6.2px;line-height:7px}
.card.back{top:426px;background:radial-gradient(ellipse at 50% 35%,#2a6ab0,#17498a 80%)}
.card.back .brand{position:absolute;left:0;right:0;top:65px;text-align:center;font-size:7.4px}
.card.back .web{position:absolute;left:0;right:0;top:88px;text-align:center;font-size:4.2px;color:#dfe8f3}

/* envelopes */
.envelope{top:730px;width:391px;height:177px}
.envelope.front{left:187px}
.envelope.front .brand{position:absolute;right:27px;top:46px;font-size:7px}
.envelope.front .contact{position:absolute;left:27px;top:107px}
.envelope.back{left:623px;background:#f2f2f2}
.envelope.back .seams{position:absolute;inset:0;width:100%;height:100%}
.envelope.back .flap{position:absolute;left:0;top:0;width:100%;height:64px}
.envelope.back .brand{position:absolute;left:0;right:0;top:27px;text-align:center;font-size:10px}
</style>
</head>
<body>

<!-- Presentation folder -->
<section class="folder">
  <div class="spine" style="left:19px"></div>
  <div class="spine" style="left:34px"></div>
  <div class="brand light">Harbor Key Advisors LLC</div>
</section>

<!-- Letterhead -->
<section class="sheet letterhead">
  <div class="brand">Harbor Key Advisors LLC</div>
  <div class="divider" style="left:131px"></div>
  <div class="contact" style="left:137px">
    <div class="row"><svg viewBox="0 0 10 10"><path d="M2 1l2 2-1 1.5c.6 1.2 1.3 1.9 2.5 2.5L7 6l2 2-1.5 1.5C4 9 1 6 .5 2.5z"/></svg>(555) 214-0190</div>
    <div class="row"><svg viewBox="0 0 10 10"><path d="M0 2h10v6H0zM1 3l4 3 4-3"/></svg>info@HarborKeyAdvisors.com</div>
    <div class="row"><svg viewBox="0 0 10 10"><circle cx="5" cy="5" r="4.5"/></svg>www.HarborKeyAdvisors.com</div>
  </div>
  <div class="divider" style="left:238px"></div>
  <div class="contact" style="left:245px">
    Harbor Key Advisors (HKA)<br>1180 Harbor St Suite 12, New York<br>NY 10014, USA
  </div>

  <div class="letter">
    <p>01 January 2050</p>
    <p class="addr"><strong>Company (Pvt) Ltd.</strong><br>PO Box 3355 Mainville St<br>Sample City Country 3355</p>
    <p style="margin-top:13px">Dear Laura Bennett,</p>
    <p>Lorem ipsum dolor sit amet, consectetuer adipiscing elit, sed diam nonummy nibh euismod tincidunt ut laoreet dolore magna aliquam erat volutpat. Ut wisi enim ad minim veniam, quis nostrud exerci tation ullamcorper suscipit lobortis nisl ut aliquip ex ea commodo consequat. Duis dolore te feugait nulla facilisi. Nam liber tempor cum soluta nobis eleifend option congue nihil imperdiet doming id quod mazim placerat facer possim assum. Lorem ipsum dolor sit amet, consectetuer adipiscing elit, sed diam nonummy nibh euismod tincidunt ut laoreet dolore magna aliquam erat volutpat. Ut wisi enim ad minim veniam, quis nostrud exerci tation ullamcorper suscipit lobortis nisl ut aliquip ex ea commodo consequat.</p>
    <p>Consectetuer adipiscing elit, sed diam nonummy nibh euismod tincidunt ut laoreet dolore magna aliquam erat volutpat. Ut wisi enim ad minim veniam, quis nostrud exerci tation ullamcorper suscipit lobortis nisl ut aliquip ex ea commodo consequat. Consectetuer adipiscing elit, sed diam nonummy nibh euismod tincidunt ut laoreet dolore magna aliquam erat volutpat. Ut wisi enim ad minim veniam, quis nostrud exerci tation ullamcorper suscipit lobortis nisl ut aliquip ex ea commodo consequat.</p>
    <p>Consectetuer adipiscing elit, sed diam nonummy nibh euismod tincidunt ut laoreet dolore magna aliquam erat volutpat. Ut wisi enim ad minim veniam, quis nostrud exerci tation ullamcorper suscipit lobortis nisl ut aliquip ex ea commodo consequat. Consectetuer adipiscing elit, sed diam nonummy nibh euismod tincidunt ut laoreet dolore magna aliquam erat volutpat. Ut wisi enim ad minim veniam, quis nostrud exerci tation ullamcorper suscipit lobortis nisl ut aliquip ex ea commodo consequat.</p>
    <p style="margin-top:20px;margin-bottom:6px">Sincerely Yours</p>
    <p class="sign">Martin Cole Avery</p>
  </div>

  <svg class="wave" viewBox="0 0 373 22" height="22" preserveAspectRatio="none">
    <path d="M0 22Q170 2 373 6L373 9Q170 5 0 22Z" fill="var(--sky)"/>
    <path d="M0 22Q170 8 373 12L373 22Z" fill="var(--navy)"/>
  </svg>
</section>

<!-- Business card front -->
<section class="sheet card front">
  <div class="brand">Harbor Key Advisors LLC</div>
  <div class="divider"></div>
  <div class="details">
    <div class="name">Daniel Reyes</div>
    <div>Managing Director</div>
    <div style="margin-top:5px">1180 Harbor St Suite 12, New York<br>NY 10014, USA</div>
    <div style="margin-top:4px">(555) 214-0190<br>info@HarborKeyAdvisors.com<br>www.HarborKeyAdvisors.com</div>
  </div>
  <svg class="wave" viewBox="0 0 188 10" height="10" preserveAspectRatio="none">
    <path d="M0 10Q90 0 188 3L188 5Q90 3 0 10Z" fill="var(--sky)"/>
    <path d="M0 10Q90 4 188 6L188 10Z" fill="var(--navy)"/>
  </svg>
</section>

<!-- Business card back -->
<section class="sheet card back">
  <div class="brand light">Harbor Key Advisors LLC</div>
  <div class="web">www.<b>HarborKeyAdvisors</b>.com</div>
</section>

<!-- Envelope front -->
<section class="sheet envelope front">
  <div class="brand">Harbor Key Advisors LLC</div>
  <div class="contact">
    Harbor Key Advisors (HKA)<br>1180 Harbor St Suite 12, New York<br>NY 10014, USA
    <div style="height:5px"></div>
    <div class="row"><svg viewBox="0 0 10 10"><path d="M2 1l2 2-1 1.5c.6 1.2 1.3 1.9 2.5 2.5L7 6l2 2-1.5 1.5C4 9 1 6 .5 2.5z"/></svg>(555) 214-0190</div>
    <div class="row"><svg viewBox="0 0 10 10"><path d="M0 2h10v6H0zM1 3l4 3 4-3"/></svg>info@HarborKeyAdvisors.com</div>
    <div class="row"><svg viewBox="0 0 10 10"><circle cx="5" cy="5" r="4.5"/></svg>www.HarborKeyAdvisors.com</div>
  </div>
  <svg class="wave" viewBox="0 0 391 20" height="20" preserveAspectRatio="none">
    <path d="M0 20Q180 0 391 5L391 9Q180 4 0 20Z" fill="var(--sky)"/>
    <path d="M0 20Q180 7 391 11L391 20Z" fill="var(--navy)"/>
  </svg>
</section>

<!-- Envelope back -->
<section class="sheet envelope back">
  <svg class="seams" viewBox="0 0 391 177" preserveAspectRatio="none">
    <path d="M6 50L4 177M385 50L387 177" stroke="#d6d6d6" fill="none"/>
  </svg>
  <svg class="flap" viewBox="0 0 391 64" preserveAspectRatio="none">
    <path d="M0 0H391L380 50Q377 62 365 62H26Q14 62 11 50Z" fill="var(--navy)"/>
  </svg>
  <div class="brand light">Harbor Key Advisors</div>
</section>

</body>
</html>
```